Marlow Naturopathics business card design

Using the marlow logo designed, we would like that incorporated into a business card. A colour scheme which works with the logo and lists the following business details:

Dennis Marlow - Naturopath
Level 1, 58 Torvane Street
Wollongong NSW
(02) 4391 7084
www.dennismarlowhealth-example.com

We would also like space on the back of the card for next appointment times.

Target Market(s)

Anyone looking to improve their health

Industry/Entity Type

Business

Requirements
Must have
• Marlow Naturopathics logo, business details.
Nice to have
• Good colour schemes, attractive, eye-catching features that are easy to read.

```html
<!DOCTYPE html>
<html lang="en">
<head>
<meta charset="utf-8">
<title>Marlow Naturopathics – Business Card</title>
<link href="https://fonts.googleapis.com/css2?family=Courier+Prime:ital,wght@0,400;0,700;1,400&display=swap" rel="stylesheet">
<style>
  :root {
    --page-bg: #2b2b2b;
    --card-blue-top: #3d8fd1;
    --card-blue-bottom: #1598dc;
    --card-white: #ffffff;
    --wave-blue: #1aa6e4;
    --wave-pale: #bfe6f8;
    --ink-navy: #2c5e9c;
    --ink-white: #ffffff;
  }
  * { margin: 0; padding: 0; box-sizing: border-box; }
  html, body { width: 1200px; height: 900px; overflow: hidden; }
  body {
    background: var(--page-bg);
    font-family: "Courier Prime", "Courier New", monospace;
    position: relative;
  }
  .card {
    position: absolute;
    width: 700px;
    height: 400px;
    overflow: hidden;
    box-shadow: 0 12px 30px rgba(0,0,0,0.5);
  }
  .card--blue {
    left: 60px; top: 50px;
    background: linear-gradient(160deg, var(--card-blue-top), var(--card-blue-bottom));
    color: var(--ink-white);
  }
  .card--white {
    left: 440px; top: 470px;
    background: var(--card-white);
    color: var(--ink-navy);
  }
  .card__wave { position: absolute; inset: 0; width: 100%; height: 100%; }
  .brand {
    position: absolute;
    right: 40px; top: 48px;
    display: flex; align-items: center; gap: 10px;
    font-weight: 700; font-size: 20px; letter-spacing: 0.5px;
  }
  .brand__dot {
    width: 22px; height: 22px; border-radius: 50%;
    background: currentColor;
  }
  .card__name {
    position: absolute; left: 60px; top: 118px;
    font-weight: 700; font-size: 36px; line-height: 44px;
  }
  .card__role {
    position: absolute; left: 175px; top: 164px;
    font-style: italic; font-size: 21px; line-height: 26px;
  }
  .card__contact {
    position: absolute; left: 60px; top: 212px;
    list-style: none; font-size: 18px; line-height: 25px;
  }
</style>
</head>
<body>

  <section class="card card--blue">
    <svg class="card__wave" viewBox="0 0 700 400" preserveAspectRatio="none" aria-hidden="true">
      <path d="M0,365 C180,390 340,372 475,304 C575,250 632,165 700,146 L700,400 L0,400 Z" fill="rgba(255,255,255,0.12)"/>
      <path d="M0,358 C180,385 340,368 470,298 C570,243 630,158 700,138 L700,152 C635,170 580,258 480,314 C350,386 180,400 0,378 Z" fill="#ffffff"/>
    </svg>
    <div class="brand"><span class="brand__dot"></span>Marlow Naturopathics</div>
    <h1 class="card__name">Dennis Marlow</h1>
    <p class="card__role">-Naturopath-</p>
    <ul class="card__contact">
      <li>Level 1, 58 Torvane Street</li>
      <li>Wollongong NSW</li>
      <li>(02) 4391 7084</li>
      <li>www.dennismarlowhealth-example.com</li>
    </ul>
  </section>

  <section class="card card--white">
    <svg class="card__wave" viewBox="0 0 700 400" preserveAspectRatio="none" aria-hidden="true">
      <path d="M480,290 C560,240 630,195 700,180 L700,192 C635,205 570,250 495,298 Z" fill="var(--wave-pale)"/>
      <path d="M0,358 C180,385 340,368 470,298 C570,243 630,188 700,180 L700,194 C635,202 580,262 480,316 C350,386 180,398 0,376 Z" fill="var(--wave-blue)"/>
    </svg>
    <div class="brand"><span class="brand__dot"></span>Marlow Naturopathics</div>
    <h2 class="card__name">Dennis Marlow</h2>
    <p class="card__role">-Naturopath-</p>
    <ul class="card__contact">
      <li>Level 1, 58 Torvane Street</li>
      <li>Wollongong NSW</li>
      <li>(02) 4391 7084</li>
      <li>www.dennismarlowhealth-example.com</li>
    </ul>
  </section>

</body>
</html>
```